Traditional style Skull and crossbones craftsmans card for making custom works home decor and more

Brovik Works surrounding a skull and cross bones. Street address is 318 Marlow Ave N Essex ON. Email is BrovikWorks@mailvane.com and telephone number will be 519-430-6185. Use the attached image as a guideline would also like Support your local artist on the card. Our names are Dale and Morgan Brovik

Industry/Entity Type

It Support

Contact Information for Business Card

Standard size with a traditional style font

Font styles to use
Decorative
Script

Requirements
Must have
• 318 Marlow Ave. N Essex ON
• 519-430-6185
• Brovikworks@mailvane.com
• Welding
• Dale and Morgan Brovik
• Support your local artist
Nice to have
• Refer to images for ideas

```html
<!DOCTYPE html>
<html lang="en">
<head>
<meta charset="utf-8">
<title>Brovik Works — Business Card</title>
<link rel="stylesheet" href="https://fonts.googleapis.com/css2?family=Cinzel+Decorative:wght@400;700&family=Cinzel:wght@400;600&display=swap">
<style>
  :root {
    --slate-light: #5b5b5b;
    --slate-mid: #414141;
    --slate-dark: #232323;
    --copper: #c4662e;
    --copper-deep: #8a4a26;
    --umber: #2e2420;
    --ink-white: #ffffff;
    --ink-soft: #f3e9df;
    --bone: #efeae2;
    --bone-shade: #9a948c;
    --ring-shadow: #141414;
  }
  * { margin: 0; padding: 0; box-sizing: border-box; }
  html, body {
    width: 1200px;
    height: 666px;
    overflow: hidden;
    background: var(--slate-dark);
  }
  .card {
    position: relative;
    width: 1200px;
    height: 666px;
    overflow: hidden;
    background:
      radial-gradient(ellipse at 30% 20%, var(--slate-light) 0%, transparent 55%),
      radial-gradient(ellipse at 75% 80%, var(--slate-light) 0%, transparent 50%),
      linear-gradient(160deg, var(--slate-mid), var(--slate-dark));
  }
  .card-art {
    position: absolute;
    inset: 0;
    width: 1200px;
    height: 666px;
  }
  .brand-text,
  .role-text {
    font-family: "Cinzel Decorative", serif;
    fill: var(--ink-white);
  }
  .brand-text { font-weight: 700; }
  .brand-text--top { font-size: 56px; letter-spacing: 6px; }
  .brand-text--bottom { font-size: 74px; letter-spacing: 4px; }
  .role-text { font-size: 46px; letter-spacing: 3px; }
  .detail-text {
    font-family: "Cinzel", serif;
    fill: var(--ink-soft);
    font-size: 15px;
    letter-spacing: 1px;
  }
  .detail-text--name { font-size: 19px; font-weight: 600; }
  .detail-text--email { text-transform: none; }
</style>
</head>
<body>
<main class="card">
  <svg class="card-art" viewBox="0 0 1200 666" xmlns="http://www.w3.org/2000/svg">
    <defs>
      <linearGradient id="copper-left" x1="0" y1="0" x2="1" y2="0">
        <stop offset="0" stop-color="var(--umber)"/>
        <stop offset="0.55" stop-color="var(--copper-deep)"/>
        <stop offset="1" stop-color="var(--copper)"/>
      </linearGradient>
      <linearGradient id="copper-right" x1="1" y1="0" x2="0" y2="0">
        <stop offset="0" stop-color="var(--umber)"/>
        <stop offset="0.55" stop-color="var(--copper-deep)"/>
        <stop offset="1" stop-color="var(--copper)"/>
      </linearGradient>
      <linearGradient id="copper-seal" x1="0" y1="0" x2="0" y2="1">
        <stop offset="0" stop-color="#6e4a38"/>
        <stop offset="0.5" stop-color="#8c5535"/>
        <stop offset="1" stop-color="var(--copper)"/>
      </linearGradient>
      <radialGradient id="emblem-tone" cx="0.5" cy="0.45" r="0.55">
        <stop offset="0" stop-color="var(--bone)"/>
        <stop offset="0.7" stop-color="#d6d0c6"/>
        <stop offset="1" stop-color="var(--bone-shade)"/>
      </radialGradient>
      <path id="arc-top" d="M 410 380 A 190 190 0 0 1 790 380"/>
      <path id="arc-bottom" d="M 372 332 A 228 228 0 0 0 828 332"/>
    </defs>

    <!-- side panels -->
    <circle class="side-panel side-panel--left" cx="2" cy="332" r="265"
            fill="url(#copper-left)" stroke="#bdbdbd" stroke-width="1.5"/>
    <circle class="side-panel side-panel--right" cx="1198" cy="332" r="265"
            fill="url(#copper-right)" stroke="#bdbdbd" stroke-width="1.5"/>

    <text class="role-text role-text--left" text-anchor="middle"
          transform="translate(92 332) rotate(-90)">Designer</text>
    <text class="role-text role-text--right" text-anchor="middle"
          transform="translate(1110 332) rotate(90)">Craftsman</text>

    <!-- owner details, left panel -->
    <g class="owner-details" text-anchor="middle">
      <text class="detail-text detail-text--name"
            transform="translate(152 332) rotate(-90)">Dale &amp; Morgan Brovik</text>
      <text class="detail-text"
            transform="translate(184 332) rotate(-90)">Welding</text>
      <text class="detail-text"
            transform="translate(214 332) rotate(-90)">Support your local artist</text>
    </g>

    <!-- contact details, right panel -->
    <g class="contact-details" text-anchor="middle">
      <text class="detail-text detail-text--email"
            transform="translate(1046 332) rotate(90)">Brovikworks@mailvane.com</text>
      <text class="detail-text"
            transform="translate(1016 332) rotate(90)">318 Marlow Ave. N Essex ON</text>
      <text class="detail-text"
            transform="translate(986 332) rotate(90)">519-430-6185</text>
    </g>

    <!-- central seal -->
    <circle class="seal-shadow" cx="604" cy="337" r="268" fill="var(--ring-shadow)" opacity="0.7"/>
    <circle class="seal-ring" cx="600" cy="332" r="272" fill="none"
            stroke="var(--ink-white)" stroke-width="7"/>
    <circle class="seal-disc" cx="600" cy="332" r="260"
            fill="url(#copper-seal)" stroke="var(--ring-shadow)" stroke-width="4"/>

    <ellipse class="seal-emblem" role="img"
             aria-label="Skull and crossbones illustration"
             cx="605" cy="345" rx="160" ry="105" fill="url(#emblem-tone)"/>

    <text class="brand-text brand-text--top" text-anchor="middle">
      <textPath href="#arc-top" startOffset="50%">Brovik</textPath>
    </text>
    <text class="brand-text brand-text--bottom" text-anchor="middle">
      <textPath href="#arc-bottom" startOffset="50%">Works</textPath>
    </text>
  </svg>
</main>
</body>
</html>
```